Criação de Capa para Facebook para Consultoria de Negócios
A empresa queria:
" DANDO SUPORTE TECNICO, COMERCIAL, OPERACIONAL, TREINAMENTO E PALESTRAS MOTIVACIONAIS, BEM COMO A ELABORAÇAO DE PLANOS DE NEGOCIOS, ESTRUTURAÇAO, REESTRUTURAÇAO DE EMPRESAS DE TODOS OS PORTES, ALÉM DE ASSESSORARAMOS TAMBEM NA AREA DE RECURSOS HUMANOS. NAS AREAS DE SEGURO, FINANCEIRA, INDUSTRIAL, COMERCIAL, ETC. PRESTANDO CONSULTORIA EMPRESARIAL NA AREA DE SEGUROS, PLANOS DE NEGOCIOS, TREINAMENTO, RH, ASSESSORIA DE MARKETING, REESTRURAÇAO OPERACIONAL ETC. "

```html
<!DOCTYPE html>
<html lang="pt-BR">
<head>
<meta charset="utf-8">
<title>Capa Facebook – Veltra Consultoria</title>
<link href="https://fonts.googleapis.com/css2?family=Arimo:wght@400;700&display=swap" rel="stylesheet">
<style>
  :root {
    --page-bg: #3b3b3b;
    --brand-blue: #24468f;
    --brand-blue-dark: #16306a;
    --panel-blue: #1d5f8c;
    --panel-blue-dark: #0f3c5e;
    --charcoal: #1b1b1b;
    --charcoal-light: #3a3a3a;
    --silver: #d9dde2;
    --white: #ffffff;
    --ink: #1f1f1f;
  }
  html, body {
    margin: 0;
    width: 1200px;
    height: 1200px;
    overflow: hidden;
    background: var(--page-bg);
    font-family: "Arimo", Arial, sans-serif;
  }
  .cover {
    position: absolute;
    left: 30px;
    top: 332px;
    width: 1140px;
    height: 536px;
    display: block;
  }
  .cover text { font-family: "Arimo", Arial, sans-serif; }
  .t-white { fill: var(--white); }
  .t-bold { font-weight: 700; }
  .t-ink { fill: var(--ink); }
</style>
</head>
<body>
<svg class="cover" viewBox="0 0 440 207" xmlns="http://www.w3.org/2000/svg">
  <defs>
    <linearGradient id="topBar" x1="0" y1="0" x2="0" y2="1">
      <stop offset="0" stop-color="var(--brand-blue)"/>
      <stop offset="1" stop-color="var(--brand-blue-dark)"/>
    </linearGradient>
    <linearGradient id="darkPanel" x1="0" y1="0" x2="1" y2="1">
      <stop offset="0" stop-color="var(--charcoal-light)"/>
      <stop offset="1" stop-color="var(--charcoal)"/>
    </linearGradient>
    <linearGradient id="bluePanel" x1="0" y1="0" x2="1" y2="1">
      <stop offset="0" stop-color="var(--panel-blue)"/>
      <stop offset="1" stop-color="var(--panel-blue-dark)"/>
    </linearGradient>
    <linearGradient id="photoFill" x1="0" y1="0" x2="1" y2="1">
      <stop offset="0" stop-color="#e8ecef"/>
      <stop offset="0.6" stop-color="#b9c2ca"/>
      <stop offset="1" stop-color="#6f7780"/>
    </linearGradient>
  </defs>

  <!-- top brand bar -->
  <rect class="top-bar" x="0" y="0" width="440" height="18" fill="url(#topBar)"/>
  <rect class="top-bar-mark" x="336" y="4" width="10" height="10" fill="var(--charcoal)" stroke="var(--white)" stroke-width="0.8"/>
  <text class="t-white t-bold" x="351" y="12.6" font-size="7.6">VELTRA CONSULTORIA</text>

  <!-- main area -->
  <rect class="photo-area" x="230" y="18" width="210" height="159" fill="url(#photoFill)"
        role="img" aria-label="Fotografia de um consultor apresentando em reunião para executivos"/>
  <rect class="dark-panel" x="0" y="18" width="160" height="159" fill="url(#darkPanel)"/>

  <!-- service panel -->
  <polygon class="panel-frame" points="90,20 305,20 280,177 199,177 118,100" fill="var(--silver)"/>
  <polygon class="service-panel" points="96,24 298,24 272,173 205,173 124,100" fill="url(#bluePanel)"/>

  <!-- web banner -->
  <polygon class="web-banner" points="282,22 440,22 440,42 290,42" fill="var(--brand-blue-dark)"/>
  <text class="t-white t-bold" x="306" y="34.5" font-size="6.6">WWW.VELTRACONSULTORIA.COM.BR</text>

  <!-- name block -->
  <text class="t-white t-bold" x="9" y="71" font-size="21">VELTRA</text>
  <text class="t-white" x="20" y="81" font-size="8">CONSULTORIA</text>

  <!-- service text -->
  <g class="t-white t-bold" font-size="7" text-anchor="middle">
    <text x="200" y="54">A VELTRA oferece serviços de</text>
    <text x="200" y="63">consultoria empresarial em todo</text>
    <text x="200" y="72">o país nas seguintes áreas:</text>
  </g>
  <g class="t-white t-bold" font-size="6.8">
    <text x="146" y="91">➤  SEGUROS <tspan font-size="5.4">(GESTÃO TÉCNICA,</tspan></text>
    <text x="164" y="99" font-size="5.4">COMERCIAL E OPERACIONAL)</text>
  </g>
  <g class="t-white t-bold" font-size="3.8" text-anchor="middle">
    <text x="222" y="109">TREINAMENTOS - PALESTRAS MOTIVACIONAIS</text>
    <text x="222" y="115">PLANO DE NEGÓCIOS - ESTRUTURAÇÃO DE EMPRESAS</text>
    <text x="222" y="121">RECURSOS HUMANOS - CONSULTORIA</text>
    <text x="222" y="127">EMPRESARIAL - GESTÃO OPERACIONAL</text>
    <text x="222" y="133">ASSESSORIA DE MARKETING - GESTÃO</text>
    <text x="222" y="139">ECONÔMICA E FINANCEIRA</text>
    <text x="222" y="145">PLANEJAMENTO ESTRATÉGICO</text>
    <text x="230" y="151">ESTRUTURAÇÃO DA ÁREA COMERCIAL</text>
  </g>

  <!-- contacts -->
  <g class="contacts">
    <circle cx="105" cy="147" r="3" fill="none" stroke="var(--white)" stroke-width="0.7"/>
    <path d="M103.7 145.5 q0.4 2.4 2.6 3" fill="none" stroke="var(--white)" stroke-width="0.8"/>
    <text class="t-white t-bold" x="111" y="149" font-size="5.2">+55 (24) 3000-0000</text>
    <rect x="103" y="156" width="4" height="6.5" rx="0.8" fill="none" stroke="var(--white)" stroke-width="0.7"/>
    <text class="t-white t-bold" x="111" y="161.5" font-size="5.2">+55 (21) 90000-0000</text>
    <rect x="102" y="169.5" width="6.5" height="4.5" fill="var(--white)"/>
    <path d="M102 169.5 l3.25 2.4 l3.25 -2.4" fill="none" stroke="var(--charcoal)" stroke-width="0.5"/>
    <text class="t-white" x="111" y="174" font-size="3.9">CONTATO@VELTRACONSULTORIA.COM.BR</text>
  </g>

  <!-- bottom strip -->
  <rect class="bottom-strip" x="0" y="177" width="440" height="30" fill="var(--white)"/>
  <text class="t-ink t-bold" x="115" y="196" font-size="7.4">VELTRA CONSULTORIA</text>

  <!-- profile block -->
  <rect class="profile" x="5" y="97" width="92" height="93" fill="var(--charcoal)" stroke="var(--white)" stroke-width="3"/>
  <text class="t-white t-bold" x="51" y="147" font-size="14" text-anchor="middle">VELTRA</text>
</svg>
</body>
</html>
```